Company Presentation re-design.

We need to create a new 15-20 pager-presentation that will show KORVALE (travel management company) as a client-centric company with a human-to-human approach. As a start we ask a Designers to create a 3 page test presentation so we can choose the winner. who will then design the rest slides

Two main idears are to be shown on the slides:
• KORVALE is client-centric company who believes in partnership with corporate clients;
• KORVALE is a stable and trustworthy partner;

The test slides should be:

Slide (1) - Our strategy is Customer – centric strategy. KORVALE bases its business approach on the customer needs. 5 qualities that identify KORVALE as a customer-centric :
1. corporate culture, aimed at customers' changing needs
2. professional Key Account Manager (KAM)
3. Each product solution meets specific client needs.
4. innovation
5. security policy

Slide (2) - Our product solutions of clients needs
The main idea of this page is to describe our products for customers. KORVALE has 5 main products:
1. Business Travel
2. Service
3. On-line booking
4. MICE & Congress
5. Non-standard services

Slide (3)
This page shows the highlights of KORVALE support and it is shown in a cloud design now.

Attched pls find our current presentation

Dear Professionals! Please pay attantion that we updated the project by doubled the budjet! Wait for yiour grate ideas. 

Target Market(s)

Mid to top management (practically any industry), travel coordinators, procurement specialists, corporate buyers etc, travelers

Industry/Entity Type

Security

Requirements
Must have
• (1) The presentation must visualize the text above, with as little text itself as possible.
(2) We would appreciate ideas with INFOGRAPHIC
(3) Design of the presentation is up to the company logo in all variations. ( attached files).
(4) We would like to see designs that use grey, blue, orange and maroon colors - corporate colors of our logo.
Nice to have
• Infografics
Designs we like:
to brintaly.com+; zumoth.com; pelvanstudio.com; tarnowatt.co.uk (infografics)

```html
<!DOCTYPE html>
<html lang="en">
<head>
<meta charset="utf-8">
<title>Our Strategy – Korvale</title>
<link href="https://fonts.googleapis.com/css2?family=Bebas+Neue&family=Open+Sans:wght@300;400&display=swap" rel="stylesheet">
<style>
  :root {
    --bg: #f1f1f1;
    --blue: #4571b3;
    --orange: #f7954a;
    --grey-text: #7a7a7a;
    --brand-grey: #8a8a8a;
    --white: #ffffff;
  }
  html, body {
    margin: 0;
    padding: 0;
    overflow: hidden;
    background: var(--bg);
  }
  .slide {
    position: relative;
    width: 1200px;
    height: 900px;
    background: var(--bg);
    overflow: hidden;
    font-family: "Open Sans", Arial, sans-serif;
  }
  .title-accent {
    position: absolute;
    left: 10px;
    top: 0;
    width: 55px;
    height: 94px;
    background: var(--orange);
  }
  .slide-title {
    position: absolute;
    left: 79px;
    top: 10px;
    margin: 0;
    font-family: "Bebas Neue", Impact, sans-serif;
    font-weight: 400;
    font-size: 74px;
    line-height: 1;
    letter-spacing: 1px;
    color: var(--blue);
  }
  .brand-name {
    position: absolute;
    right: 30px;
    top: 14px;
    font-weight: 400;
    font-size: 60px;
    line-height: 1;
    color: var(--brand-grey);
    letter-spacing: -1px;
  }
  .diagram {
    position: absolute;
    left: 0;
    top: 0;
  }
  .quality {
    position: absolute;
    margin: 0;
    font-weight: 300;
    font-size: 22px;
    line-height: 28px;
    color: var(--grey-text);
  }
  .quality--culture    { left: 229px; top: 192px; }
  .quality--solution   { left: 858px; top: 311px; }
  .quality--kam        { left: 189px; top: 414px; }
  .quality--innovation { left: 861px; top: 523px; }
  .quality--security   { left: 222px; top: 630px; }
  .footer-band {
    position: absolute;
    left: 0;
    bottom: 0;
    width: 1200px;
    height: 46px;
    background: var(--blue);
  }
  .copyright {
    position: absolute;
    left: 18px;
    bottom: 12px;
    margin: 0;
    font-size: 14px;
    color: var(--white);
  }
  .page-number {
    position: absolute;
    left: 1106px;
    bottom: 10px;
    width: 50px;
    text-align: center;
    font-family: "Bebas Neue", Impact, sans-serif;
    font-size: 34px;
    line-height: 1;
    color: var(--white);
  }
</style>
</head>
<body>
<main class="slide">
  <div class="title-accent"></div>
  <h1 class="slide-title">Our Strategy</h1>
  <div class="brand-name">korvale</div>

  <svg class="diagram" width="1200" height="900" viewBox="0 0 1200 900">
    <defs>
      <linearGradient id="photo-office" x1="0" y1="0" x2="1" y2="1">
        <stop offset="0" stop-color="#d8cbbd"/>
        <stop offset="0.5" stop-color="#8f7664"/>
        <stop offset="1" stop-color="#3f3430"/>
      </linearGradient>
      <linearGradient id="photo-chart" x1="0" y1="0" x2="1" y2="1">
        <stop offset="0" stop-color="#e2e4e8"/>
        <stop offset="1" stop-color="#b9bec6"/>
      </linearGradient>
      <linearGradient id="photo-meeting" x1="0" y1="0" x2="1" y2="1">
        <stop offset="0" stop-color="#f2f3f4"/>
        <stop offset="0.6" stop-color="#9a9597"/>
        <stop offset="1" stop-color="#3e3b40"/>
      </linearGradient>
      <linearGradient id="photo-boardroom" x1="0" y1="0" x2="1" y2="1">
        <stop offset="0" stop-color="#e7ecef"/>
        <stop offset="1" stop-color="#7f8d96"/>
      </linearGradient>
      <linearGradient id="photo-airport" x1="0" y1="0" x2="1" y2="1">
        <stop offset="0" stop-color="#efefef"/>
        <stop offset="0.55" stop-color="#8a8a8a"/>
        <stop offset="1" stop-color="#1f1f1f"/>
      </linearGradient>
    </defs>

    <path class="timeline" fill="none" stroke="var(--blue)" stroke-width="1.6"
      d="M546 94
         C546 120 552 135 544 146 C540 151 542 153 546 153
         A97 97 0 1 0 615 319
         L662 285
         A97 97 0 1 1 662 423
         L615 391
         A97 97 0 1 0 615 529
         L662 496
         A97 97 0 1 1 662 634
         L615 602
         A97 97 0 1 0 546 767
         L546 854"/>
    <circle cx="546" cy="94" r="5" fill="var(--blue)"/>

    <g class="photos" stroke="var(--white)" stroke-width="3">
      <circle cx="546" cy="250" r="88" fill="url(#photo-office)" role="img" aria-label="Photo: two colleagues reviewing a laptop together"/>
      <circle cx="731" cy="354" r="88" fill="url(#photo-chart)" role="img" aria-label="Photo: pen pointing at a financial chart"/>
      <circle cx="546" cy="460" r="88" fill="url(#photo-meeting)" role="img" aria-label="Photo: business people in a meeting"/>
      <circle cx="731" cy="565" r="88" fill="url(#photo-boardroom)" role="img" aria-label="Photo: presenter at a whiteboard in a boardroom"/>
      <circle cx="546" cy="670" r="88" fill="url(#photo-airport)" role="img" aria-label="Photo: traveller walking with luggage through an airport"/>
    </g>

    <g class="pointers" fill="var(--blue)">
      <polygon points="435,250 449,242 449,258"/>
      <polygon points="842,354 828,346 828,362"/>
      <polygon points="435,460 449,452 449,468"/>
      <polygon points="842,565 828,557 828,573"/>
      <polygon points="435,670 449,662 449,678"/>
    </g>

    <polygon class="page-tab" points="1106,854 1131,828 1156,854" fill="var(--blue)"/>
  </svg>

  <p class="quality quality--culture">Corporate<br>culture aimed at<br>changing needs<br>Customers</p>
  <p class="quality quality--solution">Each product solution<br>meets specific<br>customer problems</p>
  <p class="quality quality--kam">Access point<br>intellectual expertise<br>company - KAM</p>
  <p class="quality quality--innovation">Introduction of new<br>decisions and<br>permanent innovation</p>
  <p class="quality quality--security">Caring for security<br>traveller and<br>personal data</p>

  <footer class="footer-band"></footer>
  <p class="copyright">Copyright 2014. Korvale . All Rights reserved</p>
  <div class="page-number">2</div>
</main>
</body>
</html>
```